Company Postage Label

Design a postage label that measures: 16cm long x 9cm high with a sticky back to stick on boxes. Similar to the attached from Corbane Freight.

Industry/Entity Type

Motorcycle Part

Colors

Designer to choose colors to be used in the design.

Requirements
Must have
• Company logo and address

```html
<!DOCTYPE html>
<html lang="en">
<head>
<meta charset="utf-8">
<title>Throttleline Exhaust Works – Postage Label</title>
<link rel="stylesheet" href="https://fonts.googleapis.com/css2?family=Titillium+Web:wght@400;700&display=swap">
<style>
  :root {
    --backdrop: #d6d6d6;
    --label-black: #151515;
    --label-charcoal: #232323;
    --accent-orange: #f07d1c;
    --accent-red: #d21f26;
    --steel-grey: #4a4a4a;
    --text-light: #e6e6e6;
  }
  html, body {
    margin: 0;
    padding: 0;
    width: 923px;
    height: 1200px;
    overflow: hidden;
    background: var(--backdrop);
    font-family: "Titillium Web", sans-serif;
  }
  .postage-label {
    position: absolute;
    left: 76px;
    top: 63px;
    width: 771px;
    height: 433px;
    background: radial-gradient(ellipse at 50% 45%, var(--label-charcoal) 0%, var(--label-black) 75%);
    overflow: hidden;
  }
  .corner-accents {
    position: absolute;
    inset: 0;
    width: 100%;
    height: 100%;
  }
  .social-handle {
    position: absolute;
    top: 20px;
    right: 23px;
    display: flex;
    align-items: center;
    gap: 5px;
    font-size: 11px;
    color: var(--accent-orange);
    letter-spacing: 0.2px;
  }
  .social-dot {
    width: 9px;
    height: 9px;
    border-radius: 50%;
    background: var(--accent-orange);
  }
  .brand-name {
    position: absolute;
    left: 0;
    right: 0;
    top: 150px;
    text-align: center;
    color: var(--accent-red);
    font-weight: 700;
    line-height: 1;
    text-transform: uppercase;
  }
  .brand-name .brand-main {
    display: block;
    font-size: 62px;
    letter-spacing: 1px;
  }
  .brand-name .brand-sub {
    display: block;
    margin-top: 6px;
    font-size: 30px;
    letter-spacing: 6px;
  }
  .divider-rule {
    position: absolute;
    left: 192px;
    top: 378px;
    width: 394px;
    height: 2px;
    background: var(--accent-red);
  }
  .contact-row {
    position: absolute;
    left: 30px;
    top: 390px;
    display: flex;
    align-items: baseline;
    white-space: nowrap;
  }
  .return-address {
    font-size: 10.5px;
    color: var(--text-light);
    margin-right: 14px;
  }
  .web-address {
    font-size: 12.5px;
    font-weight: 700;
    color: var(--accent-orange);
  }
  .contact-sep {
    color: var(--accent-orange);
    margin: 0 7px;
    font-size: 12px;
  }
  .email-address {
    font-size: 11.5px;
    color: var(--accent-orange);
  }
</style>
</head>
<body>
  <section class="postage-label">
    <svg class="corner-accents" viewBox="0 0 771 433" preserveAspectRatio="none" aria-hidden="true">
      <polygon points="0,0 150,0 0,40" fill="var(--steel-grey)"/>
      <polygon points="0,40 130,8 175,8 0,58" fill="var(--accent-orange)"/>
      <polygon points="771,433 771,360 600,433" fill="var(--steel-grey)"/>
      <polygon points="771,375 771,395 640,433 590,433" fill="var(--accent-orange)"/>
    </svg>

    <div class="social-handle">
      <span class="social-dot"></span>
      <span>#THROTTLELINE-EXHAUST-WORKS</span>
    </div>

    <h1 class="brand-name">
      <span class="brand-main">Throttleline</span>
      <span class="brand-sub">Exhaust Works</span>
    </h1>

    <div class="divider-rule"></div>

    <div class="contact-row">
      <span class="return-address">18 Fern Road, Calder Creek, QLD 4190</span>
      <span class="web-address">WWW.THROTTLELINE.COM.AU</span>
      <span class="contact-sep">|</span>
      <span class="email-address">SALES@THROTTLELINE.COM.AU</span>
    </div>
  </section>
</body>
</html>
```